Criação de Embalagem (unidade) para produtos naturais
" Empresa existente à 18 anos no mercado de produtos naturais do RJ , atuando na venda no atacado ( para logistas , rede raiz dourada , delicatessen e supermercados em geral) "

```html
<!DOCTYPE html>
<html lang="pt-BR">
<head>
<meta charset="utf-8">
<title>Chá – painel traseiro da embalagem</title>
<link href="https://fonts.googleapis.com/css2?family=Arimo:wght@400;700&display=swap" rel="stylesheet">
<style>
  :root{
    --cream:#fdebd3;
    --peach:#fcd3a0;
    --orange:#f58220;
    --orange-soft:#f9a85a;
    --blue:#1f3e8e;
    --ink:#2b2b2b;
    --panel:#fff7ec;
    --seal:#555555;
    --flag:#229e45;
  }
  *{margin:0;padding:0;box-sizing:border-box}
  html,body{width:1200px;height:1200px;overflow:hidden}
  body{font-family:"Arimo",Arial,sans-serif;color:var(--ink)}
  .package-back{
    position:relative;width:1200px;height:1200px;overflow:hidden;
    background:linear-gradient(180deg,var(--cream) 0%,#fde2bd 60%,var(--peach) 100%);
  }
  .artwork{position:absolute}
  .artwork--top-band{left:340px;top:0;width:860px;height:72px;
    background:linear-gradient(180deg,var(--blue) 0%,var(--blue) 55%,var(--orange) 100%)}
  .artwork--leaves{left:0;top:800px;width:1200px;height:400px;
    background:linear-gradient(160deg,rgba(252,211,160,0) 0%,var(--orange-soft) 55%,var(--orange) 100%)}
  .info-box{
    position:absolute;left:0;width:396px;
    background:var(--panel);border:4px solid var(--orange);border-left:none;
    border-radius:0 22px 22px 0;
    display:flex;align-items:center;justify-content:center;
    text-align:center;font-weight:700;font-size:17px;line-height:1.32;padding:10px 30px;
  }
  .info-box--yield{top:228px;height:216px}
  .info-box--origin{top:600px;height:163px}
  .storage-note{
    position:absolute;left:30px;top:468px;width:336px;
    text-align:center;font-weight:700;font-size:17px;line-height:1.32;
  }
  .preparation{
    position:absolute;left:528px;top:222px;width:660px;
    font-size:18.5px;line-height:27.5px;text-align:justify;
  }
  .preparation h2{font-size:18.5px;font-weight:700;line-height:27.5px}
  .producer{
    position:absolute;left:636px;top:868px;width:420px;
    font-style:normal;text-align:center;font-size:17.5px;line-height:24px;
  }
  .producer strong{display:block}
  .seal{position:absolute;top:1092px;background:var(--seal)}
  .seal--recycle{left:936px;width:60px;height:60px;border-radius:50%}
  .seal--disposal{left:1046px;width:54px;height:60px;border-radius:4px}
  .origin-flag{position:absolute;left:1135px;top:1044px;width:65px;height:60px;background:var(--flag)}
  .origin-label{position:absolute;left:1138px;top:1120px;font-weight:700;font-size:17px;line-height:1.25;white-space:nowrap}
</style>
</head>
<body>
<main class="package-back">
  <div class="artwork artwork--top-band" role="img" aria-label="Faixa decorativa azul e laranja da marca"></div>
  <div class="artwork artwork--leaves" role="img" aria-label="Ilustração de folhas laranja"></div>

  <section class="info-box info-box--yield">
    <p>ESTA EMBALAGEM PREPARA 2 A 3 LITROS DE CHÁ ou se preferir use A PROPORÇÃO DE 1 COLHER DE CHÁ DE ERVA PARA 1 XÍCARA DE ÁGUA DE 200ML.</p>
  </section>

  <section class="storage-note">
    <p>NÃO CONTÉM GLÚTEN.</p>
    <p>Conservar ao abrigo de luz, umidade e calor.</p>
  </section>

  <section class="info-box info-box--origin">
    <p>Vegetais colhidos no seu ambiente natural ou em suas estufas sob rigoroso controle de temperatura e desidratados à sombra.</p>
  </section>

  <section class="preparation">
    <h2>PREPARO DO CHÁ</h2>
    <p>FOLHAS, FLORES E ERVAS EM PÓ: Colocam-se as ervas em um recipiente e derrama-se água fervente por cima. Tampe bem e deixe em repouso por 3 minutos, coe e sirva em seguida.</p>
    <p>CASCAS, RAÍZES, TALOS E SEMENTES: Leve-os ao fogo brando e após levantar fervura, deixe em ebulição por 1 minuto. Tampe bem e deixe em repouso por 3 minutos, coe e sirva em seguida.</p>
    <p>Utilize o chá preferencialmente sem adoçantes e prepare-o diariamente, evitando guardá-lo para o dia seguinte, pois podem ocorrer fermentações e oxidações indesejáveis.</p>
    <p>Durante os dias mais quentes (principalmente no verão) experimente usar o chá levemente gelado com uma fatia de limão ou laranja (ice-tea).</p>
  </section>

  <address class="producer">
    <strong>Produzido e/ou embalado por:</strong>
    Sol do Campo Produtos Naturais Ltda.<br>
    CNPJ 00.312.658/0001-47<br>
    Estrada das Palmeiras, 120 - Rio de Janeiro - RJ<br>
    Tel.: (21) 2300-4512 / 2300-4598
  </address>

  <div class="seal seal--recycle" role="img" aria-label="Selo de reciclagem"></div>
  <div class="seal seal--disposal" role="img" aria-label="Selo de descarte correto"></div>
  <div class="origin-flag" role="img" aria-label="Bandeira do país de origem"></div>
  <div class="origin-label">Indús<br>Brasil</div>
</main>
</body>
</html>
```